Kestrel Motorworks Card

Our company is an offroad fabrication shop that does everything from product installs to complete turnkey offroad racers. We are looking to generate new business cards for the 2014 Lord of the Boulders race in February. This is one of the largest offroad races in the country. We would like to see designs that incorporate the colors used in our logo - black, red, and white.

Industry/Entity Type

Shop

Contact Information for Business Card

KESTREL Motorworks, 2871 Marbury Ln. Houston, TX, 713-542-3097, www.kestrelmotorworks.example, Tom Ellery, Keith Molnar, Owners.

Requirements
Nice to have
• Would like to see the Logo full size on the back size of the car.

```html
<!DOCTYPE html>
<html lang="en">
<head>
<meta charset="utf-8">
<title>Kestrel Motorworks – Business Cards</title>
<link href="https://fonts.googleapis.com/css2?family=PT+Sans:wght@400;700&display=swap" rel="stylesheet">
<style>
  :root {
    --paper: #ffffff;
    --card-light: #2e2e2e;
    --card-dark: #0f0f0f;
    --red: #e0201f;
    --white: #ffffff;
    --soft-white: #e8e8e8;
  }
  html, body {
    margin: 0;
    padding: 0;
    width: 1200px;
    height: 653px;
    overflow: hidden;
    background: var(--paper);
    font-family: "PT Sans", Arial, sans-serif;
  }
  .sheet {
    position: relative;
    width: 1200px;
    height: 653px;
  }
  .card {
    position: absolute;
    width: 486px;
    height: 282px;
    overflow: hidden;
    background:
      repeating-linear-gradient(0deg, rgba(255,255,255,0.025) 0 2px, transparent 2px 5px),
      repeating-linear-gradient(90deg, rgba(0,0,0,0.12) 0 2px, transparent 2px 6px),
      linear-gradient(160deg, var(--card-light) 0%, #1c1c1c 55%, var(--card-dark) 100%);
  }
  .card--diagonal { left: 46px; top: 27px; }
  .card--vertical { left: 654px; top: 27px; }
  .card--back { left: 361px; top: 344px; height: 274px; }

  .stripes {
    position: absolute;
    inset: 0;
    width: 100%;
    height: 100%;
    z-index: 0;
  }
  .stripes polygon, .stripes rect { fill: var(--red); }

  .brand {
    position: absolute;
    z-index: 1;
    left: 18px;
    top: 44px;
    width: 210px;
    text-align: center;
    color: var(--white);
    font-weight: 700;
    line-height: 1;
  }
  .brand__name {
    display: block;
    font-size: 40px;
    letter-spacing: 1px;
  }
  .brand__sub {
    display: block;
    font-size: 24px;
    margin-top: 4px;
  }

  .owners {
    position: absolute;
    z-index: 1;
    left: 250px;
    top: 26px;
    width: 230px;
    text-align: center;
    color: var(--white);
    font-size: 24px;
    line-height: 34px;
  }
  .owners__role { color: var(--red); }

  .contact {
    position: absolute;
    z-index: 1;
    left: 252px;
    top: 150px;
    color: var(--soft-white);
    font-size: 14px;
    line-height: 22px;
    white-space: nowrap;
  }
  .contact__label { color: var(--red); }
  .contact__address { margin-top: 20px; }

  .back-brand {
    position: absolute;
    inset: 0;
    display: flex;
    flex-direction: column;
    align-items: center;
    justify-content: center;
    color: var(--red);
    font-weight: 700;
    line-height: 1;
  }
  .back-brand__name { font-size: 82px; letter-spacing: 2px; }
  .back-brand__sub { font-size: 44px; margin-top: 6px; }
</style>
</head>
<body>
<main class="sheet">

  <section class="card card--diagonal" aria-label="Business card front, diagonal stripes">
    <svg class="stripes" viewBox="0 0 486 282" aria-hidden="true">
      <polygon points="104,0 142,0 0,205 0,150"/>
      <polygon points="160,0 206,0 0,292 0,230"/>
    </svg>
    <div class="brand">
      <span class="brand__name">KESTREL</span>
      <span class="brand__sub">Motorworks</span>
    </div>
    <div class="owners">
      <div>Tom Ellery</div>
      <div>Keith Molnar</div>
      <div class="owners__role">Owners</div>
    </div>
    <div class="contact">
      <div><span class="contact__label">P:</span> 713-542-3097</div>
      <div><span class="contact__label">W:</span> www.kestrelmotorworks.example</div>
      <div class="contact__address">2871 Marbury Ln.<br>Houston, TX</div>
    </div>
  </section>

  <section class="card card--vertical" aria-label="Business card front, vertical stripes">
    <svg class="stripes" viewBox="0 0 486 282" aria-hidden="true">
      <rect x="52" y="0" width="32" height="282"/>
      <rect x="98" y="0" width="36" height="282"/>
    </svg>
    <div class="brand">
      <span class="brand__name">KESTREL</span>
      <span class="brand__sub">Motorworks</span>
    </div>
    <div class="owners">
      <div>Tom Ellery</div>
      <div>Keith Molnar</div>
      <div class="owners__role">Owners</div>
    </div>
    <div class="contact">
      <div><span class="contact__label">P:</span> 713-542-3097</div>
      <div><span class="contact__label">W:</span> www.kestrelmotorworks.example</div>
      <div class="contact__address">2871 Marbury Ln.<br>Houston, TX</div>
    </div>
  </section>

  <section class="card card--back" aria-label="Business card back">
    <div class="back-brand">
      <span class="back-brand__name">KESTREL</span>
      <span class="back-brand__sub">Motorworks</span>
    </div>
  </section>

</main>
</body>
</html>
```